Tolvern Business Cards

Business card design. dont mind if new logo is suggested.
it would be for a security company.
our clients would be bigger security companies around Australia.
have a logo done but can be replaced. see attaached. like the colors.
Need company name, person name, designation, phone and email on front.
At back company logo and name. website saddress and 2 x license numbers
would like to have 2 different background color for both sidde

Industry/Entity Type

Security

Contact Information for Business Card

round corners, front should be light in color. need logo at back with webaddress and 2 x license numners

Font styles to use
Sans Serif

Colors
f37122
faa54b
f8ba93
0255a3
0592cd
85cae6
b3d448
9bcb3c
ffffff

Requirements
Must have
• see description
Nice to have
• see description
Should not have
• should not be difficult to read or hardd to find information on card.. lets say easy on eyes yet catchy

```html
<!DOCTYPE html>
<html lang="en">
<head>
<meta charset="utf-8">
<title>Tolvern Security Group – Business Cards</title>
<link href="https://fonts.googleapis.com/css2?family=Source+Sans+3:wght@400;600;700&display=swap" rel="stylesheet">
<style>
  :root {
    --bg-centre: #dcdcdc;
    --bg-edge: #adadad;
    --card-light: #ffffff;
    --card-dark: #00157f;
    --navy-text: #0f1d8c;
    --ink: #111111;
    --mark-cyan: #3ed3dd;
    --white: #ffffff;
  }
  * { margin: 0; padding: 0; box-sizing: border-box; }
  html, body {
    width: 1200px; height: 1200px; overflow: hidden;
    font-family: "Source Sans 3", "Myriad Pro", Arial, sans-serif;
  }
  .stage {
    position: relative; width: 1200px; height: 1200px;
    background: radial-gradient(circle at 50% 50%, var(--bg-centre) 0%, var(--bg-edge) 70%);
  }
  .card { position: absolute; left: 216px; width: 797px; height: 453px; }
  .card--front {
    top: 135px; background: var(--card-light);
    border-radius: 0 46px 0 46px;
  }
  .card--back {
    top: 614px; background: var(--card-dark); color: var(--white);
    border-radius: 46px 0 46px 0;
  }
  .brand { position: absolute; text-align: center; }
  .brand__dot { display: block; margin: 0 auto; border-radius: 50%; background: var(--mark-cyan); }
  .brand__name { display: block; font-weight: 700; white-space: nowrap; letter-spacing: 0.3px; }

  .card--front .brand { left: 30px; top: 132px; width: 352px; }
  .card--front .brand__dot { width: 100px; height: 100px; }
  .card--front .brand__name { margin-top: 24px; font-size: 26px; color: var(--navy-text); }

  .person { position: absolute; right: 46px; top: 50px; text-align: right; }
  .person__name { font-size: 35px; font-weight: 700; color: var(--ink); line-height: 1; }
  .person__title { font-size: 24px; color: var(--navy-text); margin-top: 6px; }

  .contact {
    position: absolute; left: 424px; top: 198px;
    font-size: 23px; color: var(--ink); line-height: 30px;
    display: grid; grid-template-columns: 38px auto;
  }
  .contact dt { white-space: nowrap; }
  .contact dd { white-space: nowrap; }
  .contact .gap { margin-top: 15px; }

  .card--back .brand { left: 0; top: 88px; width: 797px; }
  .card--back .brand__dot { width: 148px; height: 148px; }
  .card--back .brand__name { margin-top: 30px; font-size: 32px; color: var(--white); }

  .licences { position: absolute; left: 41px; top: 351px; font-size: 24px; line-height: 31px; }
  .back-web { position: absolute; right: 41px; top: 382px; font-size: 23px; line-height: 31px; }
</style>
</head>
<body>
<main class="stage">
  <section class="card card--front" aria-label="Card front">
    <div class="brand">
      <span class="brand__dot"></span>
      <span class="brand__name">TOLVERN SECURITY GROUP</span>
    </div>
    <div class="person">
      <p class="person__name">Your Full Name</p>
      <p class="person__title">Your Title</p>
    </div>
    <dl class="contact">
      <dt>A :</dt><dd>Your address line 1</dd>
      <dt></dt><dd>Your address line 2</dd>
      <dt class="gap">P :</dt><dd class="gap">012-345-6786</dd>
      <dt>M :</dt><dd>012-345-6789</dd>
      <dt>E :</dt><dd>your email address</dd>
      <dt class="gap">W :</dt><dd class="gap">www.tolvernsecurity.com.au</dd>
    </dl>
  </section>

  <section class="card card--back" aria-label="Card back">
    <div class="brand">
      <span class="brand__dot"></span>
      <span class="brand__name">TOLVERN SECURITY GROUP</span>
    </div>
    <div class="licences">
      <p>Your licence number 1</p>
      <p>Your licence number 2</p>
    </div>
    <p class="back-web">W: www.tolvernsecurity.com.au</p>
  </section>
</main>
</body>
</html>
```